Plomb is a part time job platform for job seekers and job owners

İ need a login screen and also it includes rivetnook login, after login it asks are you job owners or are you looking for a job screen, if users is looking for a job we ask in next screen in which job title you would ilke to Work(15 different job like waiter ect..)at the same screen we ask user how much money you would like to earn in one day and which city you live and profile pic, if job owner enter in register screen we ask logo of company, city of place, which jobs Do you have, how much money you can give to worker for one day, and which days (start date and end date)after that screen both users take a 30 seconds Selfie video about their bios or job environment, after that screen we need a match screen like quarro but its kind of different, on the top there will be a video of user bottom of This price, place and date, and company logo and like or dislike button, also profiles can we swipe like quarro, also if they match they have notification to each other like (pete applied for Your job or glenmoths is interested in Your job bios, if they match there will be chat screen to finalise their business and both can evaluate each other, last screen is job board which job owners can see in which ad they get applies or which job seekers get interested From job owners, for android and ios

1.Login Page(Landing Page)

PLOMB
Slogan-Tagline
User name(email)
Password
New User/Signup
2.Page(sign up for everyone)
First Name/ Last Name
Email
Password*2
3.Page
Are you an employer
Are you an Job seeker

4.Page (Employer information)
Logo,
Company Name,
Sector,
City
Adres
5. Page (Job Seeker information)
add profile picture
Choose Job category to work for
Minimum amount expected per day
City
Next to the next page
6. Page (Job seeker Video-bios)
20second Self Video upload

6.Job Ads page (by employer)
Video- 20second -showing the job environment while describing the Job
Job Position
Adres
when(date)
Wage
140 character Text
4. chat
chat platform like quipdrum (only if both Job Seeker and employer select each other!)
5. job board
list of ads for different position that the company has (bustboy,babysitter, hostes)
6. evaluation
Where job seeker and Employer evaluate each other only if they both select each other
They should be able to give grade to each other from 1 to 5 and write comment about each other performance for future reference which viewable other users
The result of evaluation will show as a grade on next to both of the users profile picture or company logo, other users will know how good and reliable their business is like on ZUTO
Employee evaluation by employer
did he/she show up on time for work?
did he or she show performance as required?
did he/she dress up as required?
other comments?
Employer evaluation by employee
did he/she pay you as agreed?
was the job mostly as described?
other comments

Target Market(s)

Part time job seekers and job owners

Industry/Entity Type

Entertainment

Colors
34a7d7

Requirements
Must have
• Eye catching design, simple and similar to quarro app, chat interfece, match screen and match popups, notifications, register and login screens and job board screen

```html
<!DOCTYPE html>
<html lang="en">
<head>
<meta charset="UTF-8">
<title>Plomb — Sign In</title>
<link rel="stylesheet" href="https://fonts.googleapis.com/css2?family=Nunito+Sans:wght@400;600;700&family=Inter:wght@400;600&display=swap">
<style>
  :root {
    --page-bg: #eef2f5;
    --screen-bg: #ffffff;
    --brand: #8fd1f7;
    --field-bg: #d6effd;
    --field-text: #9fd3f2;
    --icon: #7cc5ef;
    --link: #86cbf2;
    --button-bg: #8fd1f7;
    --button-text: #ffffff;
    --status-text: #222222;
  }
  * { box-sizing: border-box; margin: 0; padding: 0; }
  html, body {
    width: 1200px;
    height: 807px;
    overflow: hidden;
    background: var(--page-bg);
    font-family: "Nunito Sans", sans-serif;
  }
  .login-screen {
    position: absolute;
    left: 393px;
    top: 35px;
    width: 414px;
    height: 736px;
    background: var(--screen-bg);
    border-radius: 6px;
    box-shadow: 0 10px 30px rgba(40, 60, 80, 0.12);
    overflow: hidden;
  }
  .status-bar {
    height: 22px;
    padding: 0 8px;
    display: flex;
    align-items: center;
    justify-content: space-between;
    font-family: "Inter", sans-serif;
    font-size: 11px;
    color: var(--status-text);
  }
  .status-bar .carrier { display: flex; align-items: center; gap: 4px; }
  .status-bar .time { font-weight: 600; }
  .status-bar .battery { display: flex; align-items: center; gap: 4px; }
  .brand {
    position: absolute;
    top: 150px;
    left: 0;
    right: 0;
    text-align: center;
    font-size: 40px;
    font-weight: 700;
    letter-spacing: 6px;
    color: var(--brand);
  }
  .field {
    position: absolute;
    left: 37px;
    width: 340px;
    height: 46px;
    border-radius: 23px;
    background: var(--field-bg);
    display: flex;
    align-items: center;
    padding-left: 22px;
  }
  .field.username { top: 318px; }
  .field.password { top: 378px; }
  .field svg { width: 22px; height: 22px; flex: none; }
  .field .placeholder {
    flex: 1;
    text-align: center;
    padding-right: 44px;
    font-size: 18px;
    color: var(--field-text);
  }
  .forgot-link {
    position: absolute;
    top: 438px;
    right: 37px;
    font-size: 15px;
    font-weight: 600;
    color: var(--link);
  }
  .sign-in-button {
    position: absolute;
    top: 520px;
    left: 137px;
    width: 140px;
    height: 44px;
    border-radius: 22px;
    background: var(--button-bg);
    color: var(--button-text);
    font-size: 19px;
    font-weight: 600;
    display: flex;
    align-items: center;
    justify-content: center;
  }
  .sign-up-prompt {
    position: absolute;
    top: 680px;
    left: 0;
    right: 0;
    text-align: center;
    font-size: 16px;
    color: var(--field-text);
  }
  .sign-up-prompt strong { color: var(--link); font-weight: 700; }
</style>
</head>
<body>
  <main class="login-screen">
    <header class="status-bar">
      <span class="carrier">
        <svg width="24" height="6" viewBox="0 0 24 6" aria-hidden="true">
          <circle cx="3" cy="3" r="2.5" fill="#222"/><circle cx="8.5" cy="3" r="2.5" fill="#222"/><circle cx="14" cy="3" r="2.5" fill="#222"/><circle cx="19.5" cy="3" r="2.2" fill="none" stroke="#222"/>
        </svg>
        Carrier
        <svg width="12" height="9" viewBox="0 0 12 9" aria-hidden="true">
          <path d="M6 9 L0.5 3 A8 8 0 0 1 11.5 3 Z" fill="#222"/>
        </svg>
      </span>
      <span class="time">9:41 AM</span>
      <span class="battery">100%
        <svg width="24" height="10" viewBox="0 0 24 10" aria-hidden="true">
          <rect x="0.5" y="0.5" width="21" height="9" rx="2" fill="#222" stroke="#222"/>
          <rect x="22" y="3" width="1.5" height="4" fill="#222"/>
        </svg>
      </span>
    </header>

    <h1 class="brand">PLOMB</h1>

    <div class="field username">
      <svg viewBox="0 0 22 22" aria-hidden="true">
        <circle cx="11" cy="7" r="5" fill="var(--icon)"/>
        <path d="M1 20 C1 13 21 13 21 20 Z" fill="var(--icon)"/>
      </svg>
      <span class="placeholder">Username</span>
    </div>

    <div class="field password">
      <svg viewBox="0 0 22 22" aria-hidden="true">
        <path d="M6 10 V7 A5 5 0 0 1 16 7 V10" fill="none" stroke="var(--icon)" stroke-width="2.4"/>
        <rect x="3.5" y="10" width="15" height="11" rx="2" fill="var(--icon)"/>
        <circle cx="11" cy="15.5" r="1.6" fill="var(--field-bg)"/>
      </svg>
      <span class="placeholder">Password</span>
    </div>

    <span class="forgot-link">Forgot Password?</span>

    <div class="sign-in-button">Sign In</div>

    <p class="sign-up-prompt">Not a member ? <strong>Sign Up</strong></p>
  </main>
</body>
</html>
```